Dental Plan for Dogs

We are a vet clinic and I am wanting a poster designed that can then ultimately be changed/rejigged to be use on a website/facebook as a banner ad that promotes dental health in dogs. Therefore I will need the photoshop files as well as pngs/pdfs.
I want a dog and a cat in the image used for the poster with them showing healthy teeth and looking happy!
The feels is to be professional but also cute/funny. Using the orange coming through from the logo and the logo somewhere on the poster.
The text as below
Heading: Join our Dental Bluebell Plan!
Text: Keep your fur child smiling all year round while we cap their dental work at $365 if they return for a dental clean within 365 days! The plan includes full mouth dental x-rays and scale and polish of all teeth under a carefully monitored general anaesthetic! That'll give you both a reason to smile and save you over $180 per dental! *
Conditions (in smaller writing): *Any extractions and more advanced dental procedures if required will incur an additional cost that will be discussed with your prior to the procedure.
Thanks

```html
<!DOCTYPE html>
<html lang="en">
<head>
<meta charset="utf-8">
<title>Dr Whiskers – Dental Bluebell Plan Poster</title>
<link href="https://fonts.googleapis.com/css2?family=Freckle+Face&family=Roboto:wght@400;500&family=Roboto+Condensed:wght@400&family=Montserrat:wght@400;600&display=swap" rel="stylesheet">
<style>
  :root {
    --page-bg: #ecebe8;
    --poster-bg: #fafafa;
    --brown: #6b5246;
    --orange: #e2962c;
    --white: #ffffff;
    --ink: #3a2a22;
  }
  * { margin: 0; padding: 0; box-sizing: border-box; }
  html, body { width: 1200px; height: 1035px; overflow: hidden; background: var(--page-bg); }
  .poster {
    position: absolute; left: 255px; top: 30px;
    width: 690px; height: 976px;
    background: var(--poster-bg);
    overflow: hidden;
    box-shadow: 0 6px 18px rgba(0,0,0,.25);
  }
  .column {
    position: absolute; left: 185px; top: 0;
    width: 320px; height: 880px;
    background: var(--brown);
    color: var(--white);
    text-align: center;
  }
  .brand { position: absolute; top: 72px; left: 0; width: 100%; }
  .brand-name {
    display: inline-flex; align-items: center; gap: 10px;
    font-family: "Roboto", sans-serif; font-weight: 500;
    font-size: 42px; color: var(--white); line-height: 1;
  }
  .brand-dot { width: 20px; height: 20px; border-radius: 50%; background: var(--orange); }
  .brand-sub {
    margin: 10px auto 0; width: 200px;
    border-top: 1px solid var(--orange); padding-top: 3px;
    font-family: "Montserrat", sans-serif; font-weight: 600;
    font-size: 10px; letter-spacing: 2px; color: var(--white);
  }
  .brand-location {
    margin-top: 4px;
    font-family: "Roboto", sans-serif; font-size: 21px;
    color: var(--orange); letter-spacing: .5px;
  }
  .headline {
    position: absolute; top: 228px; left: 0; width: 100%;
    font-family: "Freckle Face", cursive; line-height: 1.08;
  }
  .headline .line { display: block; font-size: 42px; }
  .headline .accent { color: var(--orange); font-size: 46px; letter-spacing: 1px; }
  .headline .plan { font-size: 40px; }
  .copy {
    position: absolute; left: 0; width: 100%;
    font-family: "Roboto", sans-serif; font-size: 16.5px; line-height: 21px;
  }
  .copy-intro { top: 412px; }
  .price {
    position: absolute; top: 478px; left: 0; width: 100%;
    font-family: "Freckle Face", cursive; font-size: 48px; color: var(--orange);
  }
  .copy-return { top: 538px; }
  .copy-includes { top: 594px; }
  .smile {
    position: absolute; top: 732px; left: 0; width: 100%;
    font-family: "Roboto Condensed", sans-serif; font-size: 20px; line-height: 25px;
  }
  .saving {
    position: absolute; left: 47px; top: 797px;
    width: 228px; height: 65px; background: var(--orange);
    padding: 7px;
  }
  .saving-inner {
    height: 100%; border: 2px dashed var(--brown);
    display: flex; align-items: center; justify-content: center; gap: 4px;
    font-family: "Roboto Condensed", sans-serif; color: var(--white);
  }
  .saving-amount { font-size: 32px; }
  .saving-label { font-size: 20px; margin-top: 6px; }
  .photo { position: absolute; }
  .photo-cat {
    left: 0; top: 620px; width: 205px; height: 280px;
    background: linear-gradient(160deg, #b7a389 0%, #8d7a62 55%, #5f5243 100%);
    border-radius: 90px 90px 0 0;
  }
  .photo-dog {
    left: 472px; top: 540px; width: 218px; height: 375px;
    background: linear-gradient(170deg, #c98a45 0%, #a8672c 45%, #3b2d22 80%, #e9e2d6 100%);
    border-radius: 110px 60px 0 0;
  }
  .follow-band {
    position: absolute; left: 0; top: 880px; width: 100%; height: 38px;
    background: var(--orange);
    display: flex; align-items: center; justify-content: center; gap: 16px;
    font-family: "Montserrat", sans-serif; font-weight: 600; font-size: 19px;
    color: var(--ink); letter-spacing: 1px;
  }
  .follow-icons { display: flex; gap: 16px; }
  .follow-icons span { width: 24px; height: 24px; border-radius: 50%; border: 2px solid var(--ink); }
  .footer {
    position: absolute; left: 0; top: 918px; width: 100%; height: 58px;
    background: var(--brown); color: var(--white);
    font-family: "Montserrat", sans-serif; font-size: 11.5px; line-height: 15px;
    text-align: center; padding-top: 12px;
  }
</style>
</head>
<body>
  <main class="poster">
    <div class="photo photo-cat" role="img" aria-label="Photo of a tabby cat sitting and looking upward"></div>

    <section class="column">
      <div class="brand">
        <div class="brand-name"><span class="brand-dot"></span>Dr Whiskers</div>
        <div class="brand-sub">VETERINARY CLINIC</div>
        <div class="brand-location">MAPLE GROVE</div>
      </div>

      <h1 class="headline">
        <span class="line">Join our</span>
        <span class="line accent">DENTAL</span>
        <span class="line plan">Bluebell Plan!</span>
      </h1>

      <p class="copy copy-intro">Keep your fur child smiling<br>all year round while we cap<br>their dental work at</p>
      <div class="price">$365</div>
      <p class="copy copy-return">if they return for a dental<br>clean within 365 days!</p>
      <p class="copy copy-includes">The plan includes full<br>mouth dental x-rays and<br>scale and polish of all teeth<br>under a carefully monitored<br>general anaesthetic!</p>

      <p class="smile">That'll give you both a reason<br>to smile &amp; save you over</p>

      <div class="saving">
        <div class="saving-inner">
          <span class="saving-amount">$180</span>
          <span class="saving-label">per dental! *</span>
        </div>
      </div>
    </section>

    <div class="photo photo-dog" role="img" aria-label="Photo of a beagle sitting and looking upward"></div>

    <div class="follow-band">
      <span>FOLLOW US:</span>
      <div class="follow-icons"><span></span><span></span></div>
    </div>

    <footer class="footer">
      *Any extractions and more advanced dental procedures if required will incur an<br>
      additional cost that will be discussed with your prior to the procedure.
    </footer>
  </main>
</body>
</html>
```